Landscape Company in need of logo and business card update. Current logo file is attached.

I need a business card design for a Woman Owned Landscape business in Kansas City. I do Native plant installation and maintenance as well as mowing, chemical applications and residential and commercial landscaping.
My colors are navy, green and white.
I currently have a logo that can be used or you can redesign it.

Target Market(s)

Residential and commercial

Industry/Entity Type

Landscape

Contact Information for Business Card

On back of current card it lists what I do and website:
BMP/Raingarden Maintenance and Installation, Certified Chemical Applicator for Trees, shrubs, and turf; Landscape Design and Installation for residential and commercial.

Logo Text

Birchwell Landscape Partners, LLC

Font styles to use
Other font styles liked:
• See current font on logo examples

Requirements
Must have
• Phone number: 913-555-0182
• Website: www.birchwellyards.example
• Colors: Navy, Green, white
• Email: birchwellyards@mailbox.example
• Address: PO BOX 417208 Alder Springs, KS 66999
• Name of Person: Marlene Kozik, owner

```html
<!DOCTYPE html>
<html lang="en">
<head>
<meta charset="utf-8">
<title>Birchwell Landscape Partners – Business Card</title>
<link href="https://fonts.googleapis.com/css2?family=Roboto:wght@300;400;700&display=swap" rel="stylesheet">
<style>
  :root {
    --backdrop: #ececec;
    --card: #f8f8f8;
    --navy: #243a6b;
    --green: #13c07a;
    --coral: #e2494e;
    --shadow: rgba(0, 0, 0, 0.10);
  }
  * { box-sizing: border-box; margin: 0; padding: 0; }
  html, body {
    width: 918px;
    height: 1200px;
    overflow: hidden;
    background: var(--backdrop);
    font-family: "Roboto", Arial, sans-serif;
  }
  .sheet {
    position: relative;
    width: 918px;
    height: 1200px;
  }
  .card {
    position: absolute;
    top: 268px;
    width: 380px;
    height: 665px;
    background: var(--card);
    box-shadow: 0 6px 18px var(--shadow);
  }
  .card--front { left: 52px; }
  .card--back { left: 486px; }

  /* Brand lockup */
  .brand {
    display: flex;
    align-items: center;
    gap: 10px;
  }
  .brand__dot {
    width: 30px;
    height: 30px;
    border-radius: 50%;
    background: var(--coral);
    flex: none;
  }
  .brand__name {
    font-weight: 400;
    font-size: 13px;
    line-height: 1.25;
    color: var(--coral);
    text-transform: uppercase;
    letter-spacing: 0.08em;
  }
  .card--front .brand {
    position: absolute;
    top: 36px;
    left: 34px;
  }

  /* Front: name block */
  .person {
    position: absolute;
    left: 34px;
    top: 372px;
    color: var(--green);
  }
  .person__name {
    font-size: 38px;
    line-height: 1;
    white-space: nowrap;
  }
  .person__first { font-weight: 300; }
  .person__last { font-weight: 700; }
  .person__role {
    font-size: 14px;
    font-weight: 400;
    margin-top: 4px;
  }

  /* Front: contact list */
  .contact {
    position: absolute;
    left: 34px;
    bottom: 42px;
    list-style: none;
  }
  .contact__item {
    display: flex;
    align-items: center;
    gap: 10px;
    font-size: 14px;
    color: var(--navy);
    line-height: 1;
    margin-top: 10px;
    white-space: nowrap;
  }
  .contact__icon {
    width: 14px;
    height: 14px;
    flex: none;
    stroke: var(--green);
    fill: none;
    stroke-width: 1.4;
    stroke-linecap: round;
    stroke-linejoin: round;
  }

  /* Back */
  .card--back .brand {
    position: absolute;
    top: 300px;
    left: 0;
    right: 0;
    flex-direction: column;
    gap: 12px;
    text-align: center;
  }
  .card--back .brand__dot { width: 60px; height: 60px; }
  .card--back .brand__name { font-size: 15px; }
  .services {
    position: absolute;
    top: 430px;
    left: 0;
    right: 0;
    list-style: none;
    text-align: center;
    font-size: 11px;
    line-height: 15px;
    color: var(--navy);
  }
  .back-web {
    position: absolute;
    left: 0;
    right: 0;
    bottom: 42px;
    text-align: center;
    font-size: 13px;
    color: var(--navy);
  }
</style>
</head>
<body>
<main class="sheet">

  <section class="card card--front" aria-label="Business card front">
    <div class="brand">
      <span class="brand__dot"></span>
      <span class="brand__name">Birchwell<br>Landscape Partners</span>
    </div>

    <div class="person">
      <p class="person__name"><span class="person__first">Marlene</span> <span class="person__last">KOZIK</span></p>
      <p class="person__role">Owner</p>
    </div>

    <ul class="contact">
      <li class="contact__item">
        <svg class="contact__icon" viewBox="0 0 14 14"><path d="M7 13s4.5-4.6 4.5-7.7A4.5 4.5 0 0 0 2.5 5.3C2.5 8.4 7 13 7 13z"/><circle cx="7" cy="5.3" r="1.5"/></svg>
        PO BOX 417208 Alder Springs, KS 66999
      </li>
      <li class="contact__item">
        <svg class="contact__icon" viewBox="0 0 14 14"><path d="M3 1.5l2.2 2.6-1.2 1.6a7.5 7.5 0 0 0 4.3 4.3l1.6-1.2 2.6 2.2-1.4 1.6C6.5 12.4 1.6 7.5 1.4 2.9z"/></svg>
        913-555-0182
      </li>
      <li class="contact__item">
        <svg class="contact__icon" viewBox="0 0 14 14"><rect x="1.5" y="3" width="11" height="8"/><path d="M1.5 3L7 7.5 12.5 3"/></svg>
        birchwellyards@mailbox.example
      </li>
      <li class="contact__item">
        <svg class="contact__icon" viewBox="0 0 14 14"><circle cx="7" cy="7" r="2.3"/><path d="M9.3 7v1.2a1.6 1.6 0 0 0 3.2 0V7A5.5 5.5 0 1 0 10 11.6"/></svg>
        www.birchwellyards.example
      </li>
    </ul>
  </section>

  <section class="card card--back" aria-label="Business card back">
    <div class="brand">
      <span class="brand__dot"></span>
      <span class="brand__name">Birchwell<br>Landscape Partners</span>
    </div>

    <ul class="services">
      <li>BMP/Raingarden Maintenance and Installation</li>
      <li>Certified Chemical Applicator for Trees,</li>
      <li>Shrubs and Turf</li>
      <li>Landscape Design and Installation</li>
      <li>for residential and commercial</li>
    </ul>

    <p class="back-web">www.birchwellyards.example</p>
  </section>

</main>
</body>
</html>
```